Harbor Zentrik needs a new Website Design

We need a WEB site landing page (/template) design, we currently have a company logo.We like the Valtor.com web designEnclosed is our company logo.Our Current website is https://www.harborzentrik.com.au/

1 page

```html
<!DOCTYPE html>
<html lang="en">
<head>
<meta charset="utf-8">
<title>Harbor Zentrik — Unified Communications</title>
<link rel="stylesheet" href="https://fonts.googleapis.com/css2?family=Lato:wght@400;700;900&display=swap">
<style>
:root{
  --blue:#1e9bd8;
  --heading:#3b8fd6;
  --navy:#0f1e33;
  --navy-2:#1d3552;
  --ink:#333;
  --muted:#555;
  --gray-bg:#f3f3f3;
  --footer:#262626;
  --footer-text:#9a9a9a;
  --white:#fff;
}
*{box-sizing:border-box;margin:0;padding:0}
html,body{width:1200px;height:4212px;overflow:hidden;background:var(--white)}
body{font-family:'Lato',sans-serif;color:var(--ink);position:relative}
section,header,footer{position:absolute;left:0;width:1200px;overflow:hidden}
.abs{position:absolute}
.btn{position:absolute;display:flex;align-items:center;justify-content:center;gap:8px;font-weight:700;font-size:14px;color:var(--white);background:var(--blue);text-decoration:none}
.btn::after{content:"›";font-size:18px;line-height:1;margin-top:-2px}
.btn-ghost{background:transparent;border:2px solid var(--white)}
.btn-outline-blue{background:var(--white);color:var(--blue)}

/* hero */
.hero{top:0;height:575px;background:linear-gradient(100deg,#0c1a2e 0%,#16304d 55%,#2a4460 80%,#1a2e47 100%)}
.hero-art{position:absolute;left:780px;top:100px;width:300px;height:360px;border-radius:40%;background:radial-gradient(ellipse at center,rgba(200,170,150,.45),rgba(30,50,75,0) 70%)}
.top-actions{position:absolute;top:20px;right:100px;display:flex;gap:10px}
.top-actions a{font-size:11px;font-weight:700;color:var(--white);height:28px;padding:0 12px;display:flex;align-items:center;text-decoration:none}
.top-login{background:var(--blue)}
.top-signup{border:1px solid #ccc}
.brand{position:absolute;left:100px;top:58px;display:flex;align-items:center;gap:10px;color:var(--white);font-size:24px;font-weight:400;letter-spacing:.5px}
.brand-mark{width:26px;height:26px;border-radius:50%;background:var(--blue)}
.main-nav{position:absolute;top:66px;left:392px;display:flex;gap:28px;font-size:13px;color:var(--white)}
.main-nav span.drop::after{content:" ▾";font-size:10px}
.search-ico{position:absolute;top:68px;left:1086px}
.hero h1{position:absolute;left:100px;top:255px;font-size:45px;font-weight:700;line-height:54px;color:var(--white)}
.hero p{position:absolute;left:100px;top:384px;font-size:13px;color:var(--white)}

/* intro */
.intro{top:575px;height:602px;text-align:center}
.intro h2{position:absolute;top:88px;left:0;width:1200px;font-size:38px;line-height:46px;font-weight:700;color:var(--heading)}
.intro .lead{position:absolute;top:198px;left:0;width:1200px;font-size:15px;color:var(--muted)}
.features{position:absolute;top:298px;left:0;width:1200px}
.feature{position:absolute;width:160px;text-align:center;font-size:11px;font-weight:700;color:#444;line-height:15px}
.feature-art{width:82px;height:82px;margin:0 auto 25px;border-radius:14px;background:linear-gradient(160deg,#dfe9f3,#a9c2d9)}

/* feature bands */
.band{height:488px}
.band.gray{background:var(--gray-bg)}
.band h3{position:absolute;font-size:16px;font-weight:700;color:var(--blue);text-transform:uppercase}
.band .sub{position:absolute;font-size:11px;font-weight:700;color:#333}
.band .copy{position:absolute;font-size:11px;line-height:15px;color:#444;text-align:justify}
.screen-art{position:absolute;border-radius:8px;background:linear-gradient(160deg,#eef3f7 0%,#cfd9e2 60%,#a9b3bc 100%)}
.btn-sm{height:30px;width:112px;font-size:12px}

.data-list p{font-size:11px;color:#444;margin-bottom:17px}

/* split */
.split{top:3126px;height:344px}
.split-half{position:absolute;top:0;width:600px;height:344px;text-align:center;color:var(--white)}
.split-half h4{position:absolute;left:0;width:600px;top:97px;font-size:15px;font-weight:700}
.split-half .s-text{position:absolute;font-size:11px;font-weight:700;line-height:19px}
.voice{left:0;background:linear-gradient(135deg,#3a8fd4,#5ba6e0 60%,#3e8dd0)}
.support{left:600px;background:linear-gradient(135deg,#5fa6e1,#7ab6e8 60%,#5b9fd9)}

/* partners */
.partners{top:3470px;height:483px;text-align:center}
.partners h2{position:absolute;top:72px;left:0;width:1200px;font-size:39px;font-weight:700;color:var(--heading)}
.partners p{position:absolute;top:137px;left:190px;width:820px;font-size:15px;line-height:23px;color:var(--muted)}
.badge{position:absolute;top:242px;height:74px;background:#e3e6ea;border-radius:6px}
.dots{position:absolute;top:395px;left:560px;display:flex;gap:6px}
.dots i{width:6px;height:6px;border-radius:50%;background:#ccc}
.dots i.on{background:#555}

/* footer */
.site-footer{top:3953px;height:259px;background:var(--footer);color:var(--footer-text);font-size:11px}
.site-footer h5{position:absolute;top:38px;font-size:12px;font-weight:700;color:var(--white);text-transform:uppercase}
.f-col{position:absolute;top:68px;line-height:17px}
.nav-links a{display:block;color:var(--blue);text-decoration:none;font-size:12px;line-height:16px}
.subscribe{position:absolute;left:526px;top:128px;display:flex;gap:6px}
.subscribe .field{width:198px;height:28px;background:var(--white);color:#999;font-size:10px;display:flex;align-items:center;padding-left:8px}
.subscribe .go{width:78px;height:28px;background:var(--blue);color:var(--white);font-size:11px;font-weight:700;display:flex;align-items:center;justify-content:center}
.social{position:absolute;left:100px;top:155px;display:flex;gap:10px}
.social i{width:11px;height:11px;border-radius:50%;background:var(--blue)}
.copyright{position:absolute;top:226px;left:0;width:1200px;text-align:center;font-size:10px;color:#555}
</style>
</head>
<body>

<header class="hero">
  <div class="hero-art" role="img" aria-label="Photo of hands cupping a glowing cloud icon"></div>
  <div class="top-actions"><a class="top-login" href="#">LOGIN</a><a class="top-signup" href="#">SIGN UP</a></div>
  <div class="brand"><span class="brand-mark"></span>Harbor Zentrik</div>
  <nav class="main-nav">
    <span>Home</span><span class="drop">Voice</span><span>Data</span><span class="drop">Hardware</span><span class="drop">Services Request</span><span class="drop">Terms &amp; Conditions</span><span>Status</span>
  </nav>
  <svg class="search-ico" width="14" height="14" viewBox="0 0 14 14"><circle cx="6" cy="6" r="4.5" fill="none" stroke="#fff" stroke-width="2"/><line x1="9.5" y1="9.5" x2="13" y2="13" stroke="#fff" stroke-width="2"/></svg>
  <h1>Australia's Business Grade Unified<br>Communications Company</h1>
  <p>White-Label Solution for all your Communication Needs</p>
  <a class="btn" href="#" style="left:100px;top:443px;width:124px;height:38px">Read More</a>
  <a class="btn btn-ghost" href="#" style="left:237px;top:443px;width:196px;height:38px;border-color:#fff">Remote Support Access</a>
</header>

<section class="intro">
  <h2>Liberating Businesses from Traditional<br>Communications System</h2>
  <p class="lead">We have all the components to start &amp; run your own White Label Telco</p>
  <div class="features">
    <div class="feature" style="left:101px"><div class="feature-art" role="img" aria-label="Server and network icon"></div>CLOUD IP PBX</div>
    <div class="feature" style="left:270px"><div class="feature-art" role="img" aria-label="Agent at desk icon"></div>UNIFIED<br>COMMUNICATIONS</div>
    <div class="feature" style="left:437px"><div class="feature-art" role="img" aria-label="Invoice and payment terminal icon"></div>INVOICE &amp;<br>PAYMENT PLATFORM</div>
    <div class="feature" style="left:603px"><div class="feature-art" role="img" aria-label="Cloud with lock icon"></div>DATA<br>SERVICES</div>
    <div class="feature" style="left:770px"><div class="feature-art" role="img" aria-label="Headset support agent icon"></div>VOICE<br>SERVICES</div>
    <div class="feature" style="left:937px"><div class="feature-art" role="img" aria-label="Wrench and screwdriver icon"></div>SUPPORT</div>
  </div>
</section>

<section class="band gray" style="top:1177px">
  <h3 style="left:100px;top:153px">Cloud IP PBX</h3>
  <div class="sub" style="left:100px;top:190px">Multiple IP PBXs on a single instance</div>
  <p class="copy" style="left:100px;top:218px;width:524px">A Multi-Tenant CloudPBX is able to handle multiple customers (tenants) with a single instance of the software. Even though every customer has a dedicated PBX, they all share the same Orbix instance. Using the single instance for all customers cuts down operating costs significantly.</p>
  <a class="btn btn-sm" href="#" style="left:100px;top:305px">Read More</a>
  <div class="screen-art" role="img" aria-label="Desktop monitor showing the PBX system dashboard" style="left:736px;top:46px;width:363px;height:388px"></div>
</section>

<section class="band" style="top:1664px">
  <div class="screen-art" role="img" aria-label="Two smartphones showing the contacts list and dial pad" style="left:101px;top:94px;width:327px;height:302px;background:linear-gradient(160deg,#f5f7f9,#d9e1e8)"></div>
  <h3 style="left:546px;top:136px">Unified Communications</h3>
  <div class="sub" style="left:546px;top:172px">Available on Desktop &amp; Mobile</div>
  <p class="copy" style="left:546px;top:200px;width:554px">Communicator is a Desktop &amp; Mobile Unified Communications application designed to provide business users with a set of features and benefits capable of transforming your company communications system into a real powerhouse.</p>
  <p class="copy" style="left:546px;top:258px;width:554px">It is available on Norvik OS, Pelago OS, Tundra Linux as a desktop application, and on Corvo Mobile and Lumen Mobile as a mobile application.</p>
  <a class="btn btn-sm" href="#" style="left:546px;top:322px">Read More</a>
</section>

<section class="band gray" style="top:2152px">
  <h3 style="left:100px;top:150px">Invoice &amp; Payment Platform</h3>
  <div class="sub" style="left:100px;top:186px">All pieces in one for an assertive management</div>
  <p class="copy" style="left:100px;top:214px;width:524px">Access Portal is a fully-featured telecom customer portal, designed for integration with one or many CloudPBX telephony switches. Access Portal has a friendly GUI that enables efficient, automated billing, invoicing and payments, allowing you to spend less time dealing with the administration of your company and more time to SELL!</p>
  <a class="btn btn-sm" href="#" style="left:100px;top:308px">Read More</a>
  <div class="screen-art" role="img" aria-label="Desktop monitor showing the customer portal dashboard" style="left:736px;top:49px;width:363px;height:386px"></div>
</section>

<section class="band" style="top:2639px">
  <div class="screen-art" role="img" aria-label="Isometric laptop with a cloud on screen inside a blue ring" style="left:131px;top:78px;width:363px;height:332px;border-radius:50%;background:radial-gradient(ellipse at center,#8fbde9 0%,#c5dff5 45%,#eef6fc 70%,#fff 72%)"></div>
  <h3 style="left:546px;top:137px">Data Services</h3>
  <div class="data-list abs" style="left:546px;top:176px">
    <p>Data Networks * not all services available all areas</p>
    <p>Fibre</p>
    <p>Ethernet – Symmetrical upload and downloads</p>
    <p>Netline – choose from three Internet speeds all with unlimited downloads</p>
  </div>
  <a class="btn btn-sm" href="#" style="left:546px;top:323px">Read More</a>
</section>

<section class="split">
  <div class="split-half voice" role="img" aria-label="Blue-tinted photo of a hand holding a smartphone">
    <h4>VOICE SERVICES</h4>
    <p class="s-text" style="left:140px;width:420px;top:132px">Everything for your Business Communications. Inbound Services, Call Termination, 1300 &amp; 1800 Services. Phone Number, Number Porting, Virtual Fax, Sip Trunk and Connectivity, SMS, Conference Bridge</p>
    <a class="btn btn-outline-blue" href="#" style="left:295px;top:217px;width:115px;height:28px;font-size:12px">Read More</a>
  </div>
  <div class="split-half support" role="img" aria-label="Blue-tinted photo of a support team wearing headsets">
    <h4>SUPPORT</h4>
    <p class="s-text" style="left:0;width:600px;top:132px">We are here to help</p>
    <p class="s-text" style="left:65px;width:440px;top:160px;font-weight:400">Our technical support team is always available to you via phone, live chat and support ticketing system.</p>
    <a class="btn btn-outline-blue" href="#" style="left:192px;top:217px;width:106px;height:28px;font-size:12px">Read More</a>
  </div>
</section>

<section class="partners">
  <h2>Meet Our Partners</h2>
  <p>Lorem ipsum, or lipsum as it is sometimes known, is dummy text used in laying out print, graphic or web designs. The passage is attributed to an unknown typesetter in the 15th century who is thought to have scrambled parts.</p>
  <div class="badge" style="left:170px;width:70px"></div>
  <div class="badge" style="left:302px;width:268px"></div>
  <div class="badge" style="left:633px;width:234px"></div>
  <div class="badge" style="left:925px;width:105px"></div>
  <div class="dots"><i></i><i></i><i class="on"></i><i></i><i></i><i></i><i></i></div>
</section>

<footer class="site-footer">
  <h5 style="left:100px">Contact Us</h5>
  <div class="f-col" style="left:100px">
    ABN: 48 205 917 362<br>
    PO Box 2190, Ashvale ACT 2611<br>
    Administration: admin@harborzentrik.com.au | +61 2 5550 1482<br>
    Accounts: accounts@harborzentrik.com.au | +61 2 5550 1482<br>
    Support: support@harborzentrik.com.au | +61 2 5550 1497
  </div>
  <div class="social"><i></i><i></i><i></i><i></i></div>

  <h5 style="left:526px">Stay Connected</h5>
  <div class="f-col" style="left:526px;width:310px;color:#777">Lorem ipsum, or lipsum as it is sometimes known, is dummy text used in laying out print, graphic or web designs.</div>
  <div class="subscribe"><div class="field">Email address</div><div class="go">Sign-Up ›</div></div>

  <h5 style="left:978px">Navigate</h5>
  <div class="f-col nav-links" style="left:978px">
    <a href="#">Home</a><a href="#">Voice</a><a href="#">Data</a><a href="#">Hardware</a><a href="#">Services Request</a><a href="#">Terms &amp; Conditions</a><a href="#">Status</a>
  </div>
  <div class="copyright">Copyright © 2003 - 2019 Harbor Zentrik | Terms of Use | Privacy and Cookie policy</div>
</footer>

</body>
</html>
```